Road Construction Company needs business cards

We would like a new business card designed for our business.

We're a road construction company based in Qld, Australia.

Can the business card please have the following information on it.

Name: Brent Malvoy
Position: General Manager
Phone: 0471 592 304
Email: Brent.malvoy@quendix.com.au
Address: 87 Harrowgate Ave, Pindarra, QLD, 4000
Website: www.quendix.com.au

Visually we'd like the card to be professional and simple.

Attached is our logo.

Our website is www.quendix.com.au

Target Market(s)

Men aged 25-60

Contact Information for Business Card

As listed in project description

Font styles to use
Serif

Requirements
Must have
• Large logo on back of card

```html
<!DOCTYPE html>
<html lang="en">
<head>
<meta charset="utf-8">
<title>Quendix Road Construction – Business Card</title>
<link rel="stylesheet" href="https://fonts.googleapis.com/css2?family=Exo+2:wght@300;400;600;700&display=swap">
<style>
  :root {
    --page: #2b2f36;
    --card: #030303;
    --blue: #1a86d9;
    --blue-deep: #1668c4;
    --cyan: #12a6d6;
    --white: #ffffff;
    --muted: #cfd3d8;
    --photo-light: #bfbfbf;
    --photo-dark: #4a4a4a;
  }
  * { box-sizing: border-box; margin: 0; padding: 0; }
  html, body { width: 1200px; height: 1200px; overflow: hidden; }
  body {
    background: var(--page);
    font-family: "Exo 2", sans-serif;
    display: flex;
    flex-direction: column;
    align-items: center;
    justify-content: center;
    gap: 60px;
  }
  .card {
    position: relative;
    width: 900px;
    height: 514px;
    background: var(--card);
    border-radius: 10px;
    overflow: hidden;
    box-shadow: 0 10px 30px rgba(0,0,0,.45);
  }
  .card-art { position: absolute; inset: 0; width: 100%; height: 100%; }

  /* front */
  .identity { position: absolute; left: 60px; top: 62px; }
  .identity .name {
    color: var(--white);
    font-weight: 700;
    font-size: 40px;
    letter-spacing: -0.5px;
    text-transform: uppercase;
    line-height: 1;
  }
  .identity .role {
    color: var(--muted);
    font-weight: 300;
    font-size: 22px;
    letter-spacing: 0.5px;
    text-transform: uppercase;
    margin-top: 6px;
  }
  .identity .rule {
    width: 44px; height: 4px; background: var(--cyan); margin-top: 12px;
  }
  .contacts { position: absolute; left: 60px; top: 212px; list-style: none; }
  .contacts li { display: flex; align-items: flex-start; gap: 22px; margin-bottom: 22px; }
  .contacts .icon { width: 44px; height: 44px; flex: none; }
  .contacts .lines { color: var(--white); font-weight: 300; font-size: 20px; line-height: 1.35; padding-top: 9px; white-space: nowrap; }

  /* back */
  .brand {
    position: absolute;
    left: 540px; top: 300px;
    display: flex; align-items: center; gap: 12px;
  }
  .brand .mark { width: 14px; height: 14px; background: var(--blue-deep); }
  .brand .wordmark {
    color: var(--blue-deep);
    font-weight: 700;
    font-size: 46px;
    letter-spacing: 3px;
    text-transform: uppercase;
  }
</style>
</head>
<body>

  <section class="card card-front" aria-label="Business card front">
    <svg class="card-art" viewBox="0 0 900 514">
      <defs>
        <linearGradient id="photoFront" x1="0" y1="0" x2="1" y2="1">
          <stop offset="0" stop-color="var(--photo-light)"/>
          <stop offset="1" stop-color="var(--photo-dark)"/>
        </linearGradient>
      </defs>
      <polygon role="img" aria-label="Black and white photo of road workers operating machinery on a roadworks site"
               points="690,0 900,0 900,514 550,514" fill="url(#photoFront)"/>
      <polygon class="band-main" points="650,0 710,0 610,300 560,300" fill="var(--blue)"/>
      <polygon class="band-cyan" points="560,300 585,300 528,514 500,514" fill="var(--cyan)" opacity=".85"/>
      <polygon class="band-lower" points="628,318 655,318 586,514 556,514" fill="var(--blue-deep)"/>
    </svg>

    <div class="identity">
      <h1 class="name">Brent Malvoy</h1>
      <p class="role">General Manager</p>
      <div class="rule"></div>
    </div>

    <ul class="contacts">
      <li>
        <svg class="icon" viewBox="0 0 44 44"><rect width="44" height="44" fill="var(--blue)"/>
          <path d="M15 12c2 0 3 4 3 5s-2 2-2 3c1 3 4 6 7 7 1 0 2-2 3-2s5 1 5 3-2 4-4 4c-7 0-15-8-15-15 0-2 1-5 3-5z" fill="var(--white)"/></svg>
        <div class="lines">0471 592 304</div>
      </li>
      <li>
        <svg class="icon" viewBox="0 0 44 44"><rect width="44" height="44" fill="var(--blue)"/>
          <g fill="none" stroke="var(--white)" stroke-width="2"><circle cx="22" cy="22" r="11"/><ellipse cx="22" cy="22" rx="5" ry="11"/><line x1="11" y1="22" x2="33" y2="22"/></g></svg>
        <div class="lines">Brent.malvoy@quendix.com.au<br>www.quendix.com.au</div>
      </li>
      <li>
        <svg class="icon" viewBox="0 0 44 44"><rect width="44" height="44" fill="var(--blue)"/>
          <path d="M22 10a8 8 0 0 1 8 8c0 6-8 15-8 15s-8-9-8-15a8 8 0 0 1 8-8z" fill="var(--white)"/><circle cx="22" cy="18" r="3" fill="var(--blue)"/></svg>
        <div class="lines">87 Harrowgate Ave, Pindarra, QLD, 4000</div>
      </li>
    </ul>
  </section>

  <section class="card card-back" aria-label="Business card back">
    <svg class="card-art" viewBox="0 0 900 514">
      <defs>
        <linearGradient id="photoBack" x1="0" y1="0" x2="1" y2="1">
          <stop offset="0" stop-color="var(--photo-light)"/>
          <stop offset="1" stop-color="var(--photo-dark)"/>
        </linearGradient>
      </defs>
      <polygon role="img" aria-label="Black and white photo of a road worker using a jackhammer beside traffic barriers"
               points="0,0 900,0 900,150 0,370" fill="url(#photoBack)"/>
      <polygon class="band-main" points="520,230 900,135 900,170 560,265" fill="var(--blue)"/>
      <polygon class="band-lower" points="80,330 420,245 400,270 80,355" fill="var(--blue-deep)"/>
      <polygon class="band-cyan" points="60,370 360,295 330,310 60,385" fill="var(--cyan)" opacity=".85"/>
    </svg>

    <div class="brand">
      <span class="mark"></span>
      <span class="wordmark">Quendix</span>
    </div>
  </section>

</body>
</html>
```